Visitenkarten-Design für private Praxis für Sprachtherapie
Zielgruppe
Private Praxis für Sprachtherapie (Logopädie)
Aufgabenstellung
Siehe PDF der Anlage.

```html
<!DOCTYPE html>
<html lang="de">
<head>
<meta charset="utf-8">
<title>Visitenkarte Praxis für Sprachtherapie</title>
<link href="https://fonts.googleapis.com/css2?family=Fira+Sans:ital,wght@0,400;0,500;0,600;0,900;1,400;1,600&family=Fira+Sans+Condensed:wght@400;600&display=swap" rel="stylesheet">
<style>
  :root {
    --navy: #1e3a6e;
    --blue: #1469a6;
    --pale: #e4eff8;
    --white: #ffffff;
    --label: #b8b8b8;
    --edge: #3a3a3a;
  }
  * { margin: 0; padding: 0; box-sizing: border-box; }
  html, body { width: 1200px; height: 1200px; overflow: hidden; background: var(--white); }
  body { position: relative; font-family: "Fira Sans", sans-serif; color: var(--navy); }

  .card {
    position: absolute; top: 238px; width: 443px; height: 684px;
    background: var(--pale); border: 1px solid var(--edge); overflow: hidden;
    box-shadow: 8px 10px 12px rgba(0,0,0,0.28);
  }
  .card--front { left: 108px; }
  .card--back { left: 657px; }
  .card__head { position: absolute; left: 0; top: 0; width: 100%; height: 161px; background: var(--white); }

  .side-label {
    position: absolute; top: 968px; font-size: 26px; letter-spacing: 1.5px;
    color: var(--label); font-weight: 400;
  }
  .side-label--front { left: 126px; }
  .side-label--back { left: 666px; }

  /* practice name block */
  .practice {
    position: absolute; color: var(--navy); line-height: 1.1;
    font-family: "Fira Sans Condensed", sans-serif; font-weight: 600;
  }
  .card--front .practice { left: 81px; top: 78px; font-size: 25px; }
  .card--front .practice .practice__owner { font-size: 38px; }
  .practice__dot {
    position: absolute; left: 374px; top: 84px; width: 52px; height: 52px;
    border: 2px solid var(--navy); border-radius: 50%;
  }

  .person { position: absolute; left: 0; width: 100%; text-align: center; }
  .person__name { top: 230px; font-size: 30px; font-weight: 500; color: var(--blue); }
  .person__role { top: 272px; font-size: 22px; font-style: italic; letter-spacing: 1px; }
  .contact {
    position: absolute; left: 0; top: 342px; width: 100%; text-align: center;
    font-family: "Fira Sans Condensed", sans-serif; font-size: 24px; line-height: 31px;
  }
  .website {
    position: absolute; left: 0; top: 628px; width: 100%; text-align: center;
    font-family: "Fira Sans Condensed", sans-serif; font-weight: 600; font-size: 24px;
  }

  .waves {
    position: absolute; left: 0; top: 449px; width: 100%; height: 166px;
    background: linear-gradient(180deg, rgba(30,58,110,0) 0%, rgba(30,58,110,0.28) 45%, rgba(30,58,110,0.12) 75%, rgba(30,58,110,0) 100%);
  }

  /* back side */
  .vowels { position: absolute; left: 0; top: 0; width: 443px; height: 161px; }
  .vowels text { font-family: "Fira Sans", sans-serif; font-weight: 900; font-size: 190px; }
  .vowel--dark { fill: var(--navy); }
  .vowel--light { fill: var(--pale); }
  .termin-title {
    position: absolute; left: 0; top: 126px; width: 100%; text-align: center;
    font-size: 26px; font-style: italic; font-weight: 600; letter-spacing: 0.5px;
  }
  .termin-table {
    position: absolute; left: 28px; top: 189px; width: 385px;
    border-collapse: collapse; background: var(--white);
  }
  .termin-table th {
    height: 39px; text-align: left; padding-left: 13px; font-size: 25px; font-weight: 500;
    color: var(--blue); border-bottom: 1.5px solid var(--blue);
  }
  .termin-table td { height: 50px; border-bottom: 1.5px solid var(--blue); }
  .termin-table th:first-child, .termin-table td:first-child { width: 193px; border-right: 1.5px solid var(--blue); }
  .card--back .practice {
    left: 0; width: 100%; top: 618px; text-align: center; font-size: 24px;
  }
  .card--back .practice .practice__owner { font-size: 28px; }
</style>
</head>
<body>

<section class="card card--front">
  <div class="card__head"></div>
  <div class="practice">Praxis für Sprachtherapie<br><span class="practice__owner">Katrin Wehlau</span></div>
  <span class="practice__dot"></span>

  <div class="person person__name">Katrin Wehlau</div>
  <div class="person person__role">INHABERIN</div>

  <div class="contact">
    Lindenallee 14, 33602 Bielefeld<br>
    Tel: 05231 418 62-7<br>
    Mail: k.wehlau@logopaedie-wehlau.de
  </div>

  <div class="waves" role="img" aria-label="Dekoratives Muster aus feinen, sich kreuzenden Wellenlinien in Dunkelblau"></div>

  <div class="website">www.logopaedie-wehlau.de</div>
</section>

<section class="card card--back">
  <div class="card__head"></div>
  <svg class="vowels" viewBox="0 0 443 161" aria-label="AEIOU">
    <text class="vowel--dark" x="-1" y="121" textLength="100" lengthAdjust="spacingAndGlyphs">A</text>
    <text class="vowel--light" x="100" y="121" textLength="72" lengthAdjust="spacingAndGlyphs">E</text>
    <text class="vowel--light" x="174" y="121" textLength="24" lengthAdjust="spacingAndGlyphs">I</text>
    <text class="vowel--dark" x="231" y="121" textLength="113" lengthAdjust="spacingAndGlyphs">O</text>
    <text class="vowel--light" x="349" y="121" textLength="70" lengthAdjust="spacingAndGlyphs">U</text>
  </svg>
  <div class="termin-title">Ihr nächster Termin</div>

  <table class="termin-table">
    <thead><tr><th>Datum</th><th>Uhrzeit</th></tr></thead>
    <tbody>
      <tr><td></td><td></td></tr>
      <tr><td></td><td></td></tr>
      <tr><td></td><td></td></tr>
      <tr><td></td><td></td></tr>
    </tbody>
  </table>

  <div class="waves" role="img" aria-label="Dekoratives Muster aus feinen, sich kreuzenden Wellenlinien in Dunkelblau"></div>

  <div class="practice">Praxis für Sprachtherapie<br><span class="practice__owner">Katrin Wehlau</span></div>
</section>

<div class="side-label side-label--front">VORDERSEITE</div>
<div class="side-label side-label--back">RÜCKSEITE</div>

</body>
</html>
```